Lanterne architecture business cards

We are a new company based in New Zealand. We Specialize in High end Luxury Residential Architecture.

Every home is bespoke and is designed to each clients individual requirements and needs.

I like to design buildings that inspire people through light and form while offering a high level of comfort and usability.

Lines of sight, proportion and balance are fundamental to the spaces I create.
Updates

August 5th is current deadline - Today's date is the 13th of August.

Target Market(s)

New Zealanders who want a custom individual home design, typically 30-65 year old males and females

Industry/Entity Type

Architecture

Contact Information for Business Card

Director - Derek Tolson
Contact Number - 0279164073
Email - info@lanternearchitecture-example.co.nz
Webstie - www.lanternearchitecture-example.co.nz
Social Media - @lanternearchitecture

Font styles to use
Sans Serif

Requirements
Must have
• Logo (Both Sides)
Website
Email
Contact Number
Social Media

Nice to have
• Texture
Should not have
• More than 3 colours - typically I would've thought 2 would be good to match the logo.

```html
<!DOCTYPE html>
<html lang="en">
<head>
<meta charset="utf-8">
<title>Lanterne architecture business cards</title>
<link rel="stylesheet" href="https://fonts.googleapis.com/css2?family=Lato:wght@300;400;700;900&display=swap">
<style>
  :root {
    --backdrop: #1c1c1c;
    --card: #f6f6f6;
    --ink: #111111;
    --rule: #8a8a8a;
  }
  * { box-sizing: border-box; margin: 0; padding: 0; }
  html, body {
    width: 1200px;
    height: 900px;
    overflow: hidden;
    background: var(--backdrop);
    font-family: "Lato", sans-serif;
    color: var(--ink);
  }
  .canvas {
    position: relative;
    width: 1200px;
    height: 900px;
  }
  .card {
    position: absolute;
    width: 700px;
    height: 400px;
    background-color: var(--card);
    background-image:
      repeating-radial-gradient(circle at 30% 40%, rgba(0,0,0,0.018) 0 1px, transparent 1px 3px),
      repeating-radial-gradient(circle at 70% 60%, rgba(0,0,0,0.014) 0 1px, transparent 1px 4px);
  }
  .card--front { left: 180px; top: 30px; }
  .card--back { left: 320px; top: 470px; }

  /* Wordmark */
  .wordmark {
    display: flex;
    flex-direction: column;
    align-items: center;
    gap: 10px;
    font-weight: 300;
    text-transform: uppercase;
  }
  .wordmark__dot {
    width: 44px;
    height: 44px;
    border-radius: 50%;
    background: var(--ink);
    margin-bottom: 8px;
  }
  .wordmark__name {
    font-size: 40px;
    letter-spacing: 0.42em;
    margin-right: -0.42em;
    line-height: 1;
  }
  .wordmark__sub {
    font-size: 13px;
    letter-spacing: 1.05em;
    margin-right: -1.05em;
    line-height: 1;
  }

  /* Front */
  .front__content {
    position: absolute;
    inset: 0;
    display: flex;
    flex-direction: column;
    align-items: center;
    justify-content: center;
    gap: 38px;
    padding-top: 20px;
  }
  .front__web {
    font-size: 14px;
    font-weight: 400;
    letter-spacing: 0.08em;
    text-transform: uppercase;
  }

  /* Back */
  .back__brand {
    position: absolute;
    left: 0;
    top: 0;
    width: 300px;
    height: 400px;
    display: flex;
    align-items: center;
    justify-content: center;
  }
  .back__brand .wordmark__name { font-size: 28px; letter-spacing: 0.36em; margin-right: -0.36em; }
  .back__brand .wordmark__sub { font-size: 10px; letter-spacing: 0.9em; margin-right: -0.9em; }
  .back__brand .wordmark__dot { width: 34px; height: 34px; }

  .divider {
    position: absolute;
    left: 300px;
    top: 95px;
    width: 1px;
    height: 200px;
    background: var(--rule);
  }
  .contact {
    position: absolute;
    left: 318px;
    top: 92px;
    right: 14px;
  }
  .contact__name {
    font-size: 27px;
    font-weight: 900;
    text-transform: uppercase;
    line-height: 1;
  }
  .contact__role {
    font-size: 14px;
    font-weight: 400;
    text-transform: uppercase;
    margin-top: 3px;
    margin-bottom: 16px;
  }
  .contact__list { list-style: none; }
  .contact__item {
    display: flex;
    align-items: center;
    gap: 8px;
    font-size: 12px;
    font-weight: 400;
    text-transform: uppercase;
    letter-spacing: 0.02em;
    line-height: 1;
    margin-bottom: 11px;
    white-space: nowrap;
  }
  .contact__item--phone { font-size: 17px; }
  .contact__icon {
    flex: 0 0 16px;
    width: 16px;
    height: 16px;
  }
  .contact__social {
    display: flex;
    align-items: center;
    gap: 8px;
    font-size: 13px;
    text-transform: uppercase;
    margin-top: 6px;
  }
  .contact__social-dot {
    width: 22px;
    height: 22px;
    border: 1.4px solid var(--ink);
    border-radius: 50%;
  }
</style>
</head>
<body>
<main class="canvas">

  <section class="card card--front" aria-label="Business card front">
    <div class="front__content">
      <div class="wordmark">
        <span class="wordmark__dot"></span>
        <span class="wordmark__name">Lanterne</span>
        <span class="wordmark__sub">Architecture</span>
      </div>
      <p class="front__web">www.lanternearchitecture-example.co.nz</p>
    </div>
  </section>

  <section class="card card--back" aria-label="Business card back">
    <div class="back__brand">
      <div class="wordmark">
        <span class="wordmark__dot"></span>
        <span class="wordmark__name">Lanterne</span>
        <span class="wordmark__sub">Architecture</span>
      </div>
    </div>

    <div class="divider"></div>

    <div class="contact">
      <h1 class="contact__name">Derek Tolson</h1>
      <p class="contact__role">Director</p>
      <ul class="contact__list">
        <li class="contact__item contact__item--phone">
          <svg class="contact__icon" viewBox="0 0 16 16" aria-hidden="true">
            <path d="M3.2 1.5 5.6 4 4.4 5.6c.8 2.2 3.1 4.6 6 6l1.6-1.2 2.5 2.4-1.6 1.7C7.5 14.1 1.9 8.5 1.5 3.1Z" fill="var(--ink)"/>
          </svg>
          0279164073
        </li>
        <li class="contact__item">
          <svg class="contact__icon" viewBox="0 0 16 16" aria-hidden="true">
            <rect x="1" y="3.5" width="14" height="9.5" fill="var(--ink)"/>
            <path d="M1.5 4 8 9 14.5 4" fill="none" stroke="var(--card)" stroke-width="1.2"/>
          </svg>
          info@lanternearchitecture-example.co.nz
        </li>
        <li class="contact__item">
          <svg class="contact__icon" viewBox="0 0 16 16" aria-hidden="true">
            <g fill="none" stroke="var(--ink)" stroke-width="1.3">
              <circle cx="8" cy="8" r="6.5"/>
              <ellipse cx="8" cy="8" rx="3" ry="6.5"/>
              <path d="M1.5 8h13M2.5 4.8h11M2.5 11.2h11"/>
            </g>
          </svg>
          www.lanternearchitecture-example.co.nz
        </li>
      </ul>
      <p class="contact__social">
        <span class="contact__social-dot"></span>
        @lanternearchitecture
      </p>
    </div>
  </section>

</main>
</body>
</html>
```